Business Card for a Floral & Decorating Business

I would like to take my current logo and create a better business card. I am looking for elegance as I am a florist and event decorator. My logo has multiple colour options. I like colours like green, purple, pink and orange, I think I would like a white card, open to black back ground. I want it to feel elegant and romantic. I like metallic lettering that maybe is indented in the paper, I also like glossy paper. I have a full logo already as well as a badge. I have attached both in multiple colours.m

Target Market(s)

Weddings, special events, floral customers

Industry/Entity Type

Floral and decorating

Contact Information for Business Card

Phone number, email, instagram, facebook, title, name, logo

Font styles to use
Script

Requirements
Nice to have
• Elegant

```html
<!DOCTYPE html>
<html lang="en">
<head>
<meta charset="utf-8">
<title>Maren Ellis – Decorating &amp; Florals Business Card</title>
<link rel="stylesheet" href="https://fonts.googleapis.com/css2?family=Great+Vibes&family=Cormorant+Garamond:wght@500&family=Arimo:wght@400;700&display=swap">
<style>
  :root {
    --backdrop: #ababab;
    --card-white: #ffffff;
    --blush: #e6b9aa;
    --blush-text: #e2b09f;
    --floral-tint: #f8e8e2;
    --floral-tint-soft: #fcf3f0;
    --contact-grey: #9d9d9d;
    --on-blush: #ffffff;
  }
  * { box-sizing: border-box; margin: 0; padding: 0; }
  html, body { width: 1200px; height: 1000px; overflow: hidden; }
  body { background: var(--backdrop); position: relative; font-family: "Arimo", Arial, sans-serif; }

  .card { position: absolute; left: 293px; width: 615px; height: 355px; overflow: hidden; }
  .card--front { top: 112px; background: var(--card-white); }
  .card--back { top: 562px; background: var(--blush); }

  .floral-panel {
    position: absolute; top: 0; width: 145px; height: 100%;
    background: linear-gradient(180deg, var(--floral-tint-soft), var(--floral-tint) 50%, var(--floral-tint-soft));
  }
  .floral-panel--left { left: 0; }
  .floral-panel--right { right: 0; }

  .centered { position: absolute; left: 0; width: 100%; text-align: center; }

  .mark-dot { position: absolute; border-radius: 50%; left: 50%; transform: translateX(-50%); }
  .card--front .mark-dot { top: 40px; width: 56px; height: 56px; border: 1.5px solid var(--blush-text); }
  .card--back .mark-dot { top: 68px; width: 90px; height: 90px; border: 2px solid var(--on-blush); }

  .brand-name { font-family: "Great Vibes", cursive; font-weight: 400; line-height: 1; }
  .card--front .brand-name { top: 118px; font-size: 50px; color: var(--blush-text); }
  .card--back .brand-name { top: 168px; font-size: 86px; color: var(--on-blush); }

  .tagline { font-family: "Cormorant Garamond", serif; font-weight: 500; text-transform: uppercase; }
  .card--front .tagline { top: 167px; font-size: 10px; letter-spacing: 2.6px; color: var(--blush-text); }
  .card--back .tagline { top: 256px; font-size: 14px; letter-spacing: 4px; color: var(--on-blush); }

  .contact { color: var(--contact-grey); }
  .contact__phone { top: 202px; font-size: 18px; font-weight: 700; }
  .contact__email { top: 225px; font-size: 17px; }
  .contact__social { font-size: 15px; display: flex; justify-content: center; align-items: center; gap: 4px; }
  .contact__social--first { top: 276px; }
  .contact__social--second { top: 300px; }
  .social-square { width: 17px; height: 17px; border: 2px solid var(--contact-grey); border-radius: 3px; display: inline-block; }
</style>
</head>
<body>
  <section class="card card--front" aria-label="Business card front">
    <div class="floral-panel floral-panel--left" role="img" aria-label="Faint blush line-art flowers and leaves along the left edge"></div>
    <div class="floral-panel floral-panel--right" role="img" aria-label="Faint blush line-art flowers and leaves along the right edge"></div>

    <span class="mark-dot" aria-hidden="true"></span>
    <p class="centered brand-name">Maren Ellis</p>
    <p class="centered tagline">Decorating &amp; Florals.</p>

    <p class="centered contact contact__phone">(555) 014-2290</p>
    <p class="centered contact contact__email">marenellis@example.com</p>
    <p class="centered contact contact__social contact__social--first"><span class="social-square" aria-hidden="true"></span>marenellisdecor.florals</p>
    <p class="centered contact contact__social contact__social--second"><span class="social-square" aria-hidden="true"></span>simplyyoursdecor</p>
  </section>

  <section class="card card--back" aria-label="Business card back">
    <span class="mark-dot" aria-hidden="true"></span>
    <p class="centered brand-name">Maren Ellis</p>
    <p class="centered tagline">Decorating &amp; Florals.</p>
  </section>
</body>
</html>
```